Commercial Real Estate Executive Recruiting Firm Needs Business Card Design

We need a business card design for BRAMLEY | Executive Recruiting - an executive recruiting firm focused exclusively on the commercial real estate industry. We place professionals ranging from Analyst to the Executive Office covering all investment/finance disciplines (acquisitions, asset management, capital markets, etc.) in all product types (office, retail, multifamily, industrial, land, etc.). We have a passion for helping people (clients and candidates) and have a reputation for being open and honest in our recruiting - and yes, very successful. We have recently developed a new logo and would like to update our business cards as well. I've uploaded some information about our company that contains the new logo.

Target Market(s)

Commercial Real Estate professionals. Primarily in the US. These are typically, smart, driven professionals with finance degrees and MBAs. Primarily men between the ages of 25 and 55.

Industry/Entity Type

Real Estate

Font styles to use
Other font styles liked:
• The font for "BRAMLEY" is Blair ITC (Medium), and "executive recruiting" is Gotham (Book).

Requirements
Must have
• I like the idea of white background on one side and solid color (blue, black, etc.) on back of card.

Would like to utilize the fonts in the logo (to the extent possible) so as to not have too many fonts on card.
Nice to have
• I think the roles (i.e., Acquisitions, Asset Management, etc.,...) is probably likely best placed on the back side of the card with the logo maybe. See attached current business card for content.

```html
<!DOCTYPE html>
<html lang="en">
<head>
<meta charset="utf-8">
<title>BRAMLEY Executive Recruiting – Business Card</title>
<link rel="stylesheet" href="https://fonts.googleapis.com/css2?family=Montserrat:ital,wght@0,400;0,500;0,600;1,400&display=swap">
<style>
  :root {
    --stage-top: #d9dcdc;
    --stage-bottom: #f4f5f5;
    --card-white: #ffffff;
    --brand-blue: #0a4f9a;
    --brand-blue-deep: #0a4788;
    --ink: #222426;
    --ink-soft: #5b5e62;
    --heading-blue: #1f5e9e;
    --on-blue: #ffffff;
  }
  * { margin: 0; padding: 0; box-sizing: border-box; }
  html, body { width: 1200px; height: 1000px; overflow: hidden; }
  body {
    background: linear-gradient(180deg, var(--stage-top) 0%, var(--stage-bottom) 45%, var(--stage-top) 100%);
    font-family: "Montserrat", sans-serif;
    position: relative;
  }
  .card {
    position: absolute;
    top: 345px;
    width: 492px;
    height: 318px;
    background: var(--card-white);
    overflow: hidden;
    box-shadow: 0 3px 8px rgba(0,0,0,0.3);
  }
  .card--front { left: 96px; }
  .card--back { left: 620px; }
  .card__band { position: absolute; inset: 0; width: 100%; height: 100%; }

  .brand { position: absolute; left: 20px; top: 28px; display: flex; align-items: center; gap: 16px; }
  .brand__square { width: 52px; height: 52px; background: var(--brand-blue); }
  .brand__name { font-weight: 500; font-size: 34px; letter-spacing: 7px; color: var(--ink); line-height: 1; }

  .contact { position: absolute; left: 167px; top: 182px; color: var(--on-blue); }
  .contact__name { font-size: 25px; font-weight: 600; letter-spacing: -0.5px; }
  .contact__title { font-size: 10px; font-weight: 500; letter-spacing: 3px; margin-left: 6px; }
  .contact__phone { margin-top: 20px; font-size: 17px; letter-spacing: 1.8px; }
  .contact__web { margin-top: 16px; font-size: 16px; letter-spacing: 1.3px; line-height: 20px; }

  .tagline { position: absolute; right: 27px; top: 14px; text-align: right; }
  .tagline__title { font-size: 23px; color: var(--heading-blue); letter-spacing: -0.2px; }
  .tagline__sub { font-size: 14.5px; font-style: italic; color: var(--ink-soft); letter-spacing: 0.8px; margin-top: 2px; margin-right: 30px; }

  .back-mark { position: absolute; left: 30px; top: 143px; opacity: 0.35; }
  .back-mark__square { display: block; width: 92px; height: 100px; background: var(--on-blue); }

  .disciplines {
    position: absolute; left: 22px; bottom: 10px; color: var(--on-blue);
    font-size: 15.5px; letter-spacing: 2.2px; line-height: 20px; white-space: nowrap;
  }
</style>
</head>
<body>
  <section class="card card--front" aria-label="Card front">
    <svg class="card__band" viewBox="0 0 492 318" preserveAspectRatio="none" role="img" aria-label="Blue colour band across the lower card">
      <defs>
        <linearGradient id="frontBand" x1="0" y1="0" x2="0" y2="1">
          <stop offset="0" stop-color="#0a4f9a"/>
          <stop offset="1" stop-color="#0a4788"/>
        </linearGradient>
      </defs>
      <path d="M0,318 L0,250 Q246,120 492,40 L492,318 Z" fill="url(#frontBand)"/>
    </svg>
    <div class="brand">
      <span class="brand__square" aria-hidden="true"></span>
      <span class="brand__name">BRAMLEY</span>
    </div>
    <div class="contact">
      <p><span class="contact__name">Jordan Hale</span><span class="contact__title">PRESIDENT</span></p>
      <p class="contact__phone">M | 214-555-0148</p>
      <p class="contact__web">jordan@bramleyrecruiting.com<br>www.bramleyrecruiting.com</p>
    </div>
  </section>

  <section class="card card--back" aria-label="Card back">
    <svg class="card__band" viewBox="0 0 492 318" preserveAspectRatio="none" role="img" aria-label="Blue colour band across the lower card">
      <defs>
        <linearGradient id="backBand" x1="0" y1="0" x2="0" y2="1">
          <stop offset="0" stop-color="#0a4f9a"/>
          <stop offset="1" stop-color="#0a4788"/>
        </linearGradient>
      </defs>
      <path d="M0,318 L0,40 Q246,120 492,250 L492,318 Z" fill="url(#backBand)"/>
    </svg>
    <div class="tagline">
      <p class="tagline__title">Comercial Real Estate Recruiting</p>
      <p class="tagline__sub">Analyst to Executive Office Placement</p>
    </div>
    <div class="back-mark" aria-hidden="true">
      <span class="back-mark__square"></span>
    </div>
    <p class="disciplines">Acquisitions | Asset Management | Banking<br>Development | Capital Markets | Brokerage</p>
  </section>
</body>
</html>
```